Webdesign für Vernetzung christlicher Geschäftsleute
Zielgruppe
Die Vereinigung KRTWLE bezweckt die Vernetzung christlicher Geschäftsleute und die Verbreitung von Biblisch fundierten ethischen Geschäftsprinzipien. Die Zielgruppe umfasst Unternehmer und Verantwortungsträger aus Wirtschaft und Politik.
Aufgabenstellung
Ich suche einen Designer, welcher sich ernsthaft mit den Anforderungen und dem Design auseinandersetzt und eine Individuelle Lösung gestaltet.
Das Logo sowie ein unverbindlicher Vorschlag für die Strukturierung liegen bei.
Bitte keine 08/15 Business Stock Fotos (Händeschütteln, Meetings, Präsentationen).
Das Design soll folgende Seiten beinhalten (Beschreibung folgt):
- Startseite
- Standardseite (Titel, Text mit Bildern)
- Event-Detail Seite (Titel, Ort, Datum, ev. Foto, Beschreibungstext, ev. Map)
- Chapter Startseite
Die bestehende Webseite ist kein Massstab ;).

```html
<!DOCTYPE html>
<html lang="de">
<head>
<meta charset="utf-8">
<title>KRTWLE – Startseite</title>
<link href="https://fonts.googleapis.com/css2?family=Open+Sans:wght@400;600;700&family=Noto+Serif:wght@400&display=swap" rel="stylesheet">
<style>
:root{
  --red:#b0102a;
  --ink:#111;
  --text:#333;
  --paper:#fff;
  --footer:#dedede;
  --tile:#f1f1f3;
  --stage:#fff;
}
*{margin:0;padding:0;box-sizing:border-box}
html,body{width:717px;height:1200px;overflow:hidden;background:var(--stage);font-family:"Open Sans",sans-serif;color:var(--ink)}
.abs{position:absolute}
.page{position:absolute;background:var(--paper);box-shadow:0 6px 24px rgba(0,0,0,.12);overflow:hidden}
.desktop{left:26px;top:30px;width:508px;height:614px}
.mobile{left:552px;top:30px;width:140px;height:775px}
.brand{display:flex;align-items:center;gap:4px;font-weight:700;color:var(--red)}
.brand .dot{border-radius:50%;background:var(--red)}
.nav a{position:absolute;font-size:6.5px;font-weight:700;color:var(--ink);text-decoration:none;letter-spacing:.2px}
.nav a.active{border-bottom:1.5px solid var(--red);padding-bottom:1px}
.hero{background:linear-gradient(160deg,#eeeeee 0%,#d9d9d9 25%,#9a9a9a 45%,#f2f2f2 65%,#e4dcdc 85%,#fafafa 100%);box-shadow:0 3px 8px rgba(0,0,0,.12)}
.chapter-menu{display:flex;align-items:center;gap:4px;font-weight:700;color:var(--ink)}
.burger{display:flex;flex-direction:column;justify-content:space-between}
.burger span{display:block;height:1.5px;background:var(--ink)}
.headline span{display:inline-block;background:var(--paper);font-weight:700;padding-right:4px;line-height:1.12}
.section-title{color:var(--red);font-weight:700;letter-spacing:.2px}
.copy{color:var(--text)}
.tile{background:var(--tile);box-shadow:0 2px 5px rgba(0,0,0,.12);display:flex;align-items:center;justify-content:center;font-family:"Noto Serif",serif;color:#555}
.tile-label{font-weight:700;color:var(--ink)}
.event-photo{background:linear-gradient(180deg,#d6d6d6 0%,#a8a8a8 55%,#6f6f6f 100%);box-shadow:0 2px 5px rgba(0,0,0,.15)}
.event-title{font-weight:700;color:var(--ink)}
.event-date{font-weight:700;color:var(--red)}
.event-venue{color:var(--text)}
.footer{background:var(--footer)}
</style>
</head>
<body>

<!-- Desktop page -->
<section class="page desktop">
  <div class="abs brand" style="left:59px;top:48px;font-size:11px"><span class="dot" style="width:9px;height:9px"></span>KRTWLE</div>
  <nav class="nav">
    <a class="active" href="#" style="left:264px;top:53px">START</a>
    <a href="#" style="left:315px;top:53px">ÜBER UNS</a>
    <a href="#" style="left:383px;top:53px">KONTAKT</a>
  </nav>
  <div class="abs hero" role="img" aria-label="Verschneiter Berggipfel im Nebel" style="left:128px;top:85px;width:299px;height:165px"></div>
  <div class="abs chapter-menu" style="left:373px;top:94px;font-size:6.5px">CHAPTER
    <div class="burger" style="width:9px;height:7px"><span></span><span></span><span></span></div>
  </div>
  <h1 class="abs headline" style="left:87px;top:122px;font-size:16px">
    <span>SEIN</span><br><span>ZEICHEN</span><br><span>ÜBER UNS</span><br><span>IST LIEBE</span>
  </h1>

  <h2 class="abs section-title" style="left:78px;top:274px;font-size:6.5px">WILLKOMMEN</h2>
  <p class="abs copy" style="left:78px;top:291px;width:204px;font-size:4.9px;line-height:7.4px">Lorem ipsum dolor sit amet, consetetur sadipscing elitr, sed diam nonumy eirmod tempor invidunt ut labore et dolore magna aliquyam erat, sed diam voluptua. At vero eos et accusam et justo duo dolores et ea rebum. Stet clita kasd gubergren, no sea takimata sanctus est Lorem ipsum dolor sit amet. Lorem ipsum dolor sit amet, consetetur sadipscing elitr, sed diam nonumy eirmod tempor invidunt ut labore et dolore magna aliquyam erat, sed diam voluptua. At vero eos et accusam et justo duo dolores et ea rebum. Stet clita kasd gubergren, no sea takimata sanctus est Lorem ipsum dolor sit amet.</p>

  <h2 class="abs section-title" style="left:78px;top:374px;font-size:6.5px">CHAPTERS</h2>
  <div class="abs tile" style="left:78px;top:393px;width:56px;height:36px;font-size:26px">I</div>
  <div class="abs tile" style="left:152px;top:393px;width:56px;height:36px;font-size:26px">II</div>
  <div class="abs tile" style="left:226px;top:393px;width:56px;height:36px;font-size:26px">III</div>
  <div class="abs tile-label" style="left:78px;top:437px;font-size:6.5px">CHAPTER 1</div>
  <div class="abs tile-label" style="left:152px;top:437px;font-size:6.5px">CHAPTER 2</div>
  <div class="abs tile-label" style="left:227px;top:437px;font-size:6.5px">CHAPTER 3</div>

  <h2 class="abs section-title" style="left:333px;top:274px;font-size:6.5px">EVENTS</h2>
  <div class="abs event-photo" role="img" aria-label="Modernes Gebäude mit Hotelschriftzug" style="left:333px;top:291px;width:94px;height:62px"></div>
  <div class="abs event-title" style="left:336px;top:363px;font-size:4.8px">GOTTES IDEE MIT DER AGENTUR K</div>
  <div class="abs event-date" style="left:336px;top:372px;font-size:4.8px">22/03/2019</div>
  <div class="abs event-venue" style="left:336px;top:381px;font-size:4.8px">ZUM ADLER | Birkenau</div>
  <svg class="abs" style="left:420px;top:381px" width="7" height="6" viewBox="0 0 7 6"><path d="M0 0l3 3-3 3M3 0l3 3-3 3" fill="none" stroke="var(--red)" stroke-width="1.2"/></svg>

  <div class="abs event-photo" role="img" aria-label="Gasthaus mit Terrasse und Sonnenschirmen" style="left:331px;top:409px;width:94px;height:61px"></div>
  <div class="abs event-title" style="left:334px;top:479px;font-size:4.8px">NÄCHSTE GENERALVERSAMMLUNG</div>
  <div class="abs event-date" style="left:334px;top:488px;font-size:4.8px">23/03/2019</div>
  <div class="abs event-venue" style="left:334px;top:497px;font-size:4.8px">AUBERGE DES PINS | Vallorbe</div>
  <svg class="abs" style="left:419px;top:497px" width="7" height="6" viewBox="0 0 7 6"><path d="M0 0l3 3-3 3M3 0l3 3-3 3" fill="none" stroke="var(--red)" stroke-width="1.2"/></svg>

  <footer class="abs footer" style="left:0;top:523px;width:508px;height:91px">
    <div class="abs" style="left:53px;top:27px;font-size:7.5px;font-weight:700">KRTWLE</div>
    <div class="abs" style="left:53px;top:41px;font-size:7.8px;line-height:11px">Kreis Treuer Wirtschafts<br>Leute Europa</div>
    <div class="abs" style="left:228px;top:41px;font-size:7.8px;line-height:11px">info@krtwle.de<br>www.krtwle.com</div>
    <div class="abs" style="left:365px;top:41px;font-size:7.8px;line-height:11px">Datenschutz<br>Impressum</div>
  </footer>
</section>

<!-- Mobile page -->
<section class="page mobile">
  <div class="abs brand" style="left:5px;top:8px;font-size:6px"><span class="dot" style="width:5px;height:5px"></span>KRTWLE</div>
  <div class="abs burger" style="left:129px;top:8px;width:8px;height:7px"><span></span><span></span><span></span></div>
  <div class="abs hero" role="img" aria-label="Verschneiter Berggipfel im Nebel" style="left:0;top:48px;width:140px;height:78px;box-shadow:none"></div>
  <h1 class="abs headline" style="left:11px;top:30px;font-size:7px">
    <span>SEIN ZEICHEN</span><br><span>ÜBER UNS IST</span><br><span>LIEBE</span>
  </h1>
  <div class="abs" style="left:114px;top:53px;font-size:3.5px;font-weight:700">CHAPTER <span style="color:var(--red)">»</span></div>

  <h2 class="abs section-title" style="left:8px;top:131px;font-size:7px">WILLKOMMEN</h2>
  <p class="abs copy" style="left:8px;top:143px;width:125px;font-size:3.9px;line-height:6px">Lorem ipsum dolor sit amet, consetetur sadipscing elitr, sed diam nonumy eirmod empor invidunt ut labore et dolore magna aliquyam erat, sed diam voluptua. Ate ero eos et accusam et justo duo dolores et ea rebum. Stet clita kasd gubergren, o sea takimata sanctus est Lorem ipsum dolor sit amet. Lorem ipsum dolor sit met, consetetur sadipscing elitr, sed diam nonumy eirmod tempor invidunt ute abore et dolore magna aliquyam erat, sed diam voluptua. At vero eos et accusam justo duo dolores et ea rebum.</p>

  <h2 class="abs section-title" style="left:12px;top:216px;font-size:7px">CHAPTERS</h2>
  <div class="abs tile" style="left:12px;top:234px;width:51px;height:33px;font-size:22px">I</div>
  <div class="abs tile" style="left:77px;top:234px;width:51px;height:33px;font-size:22px">II</div>
  <div class="abs tile" style="left:12px;top:290px;width:51px;height:33px;font-size:22px">III</div>
  <div class="abs tile-label" style="left:23px;top:274px;font-size:4.5px">CHAPTER 1</div>
  <div class="abs tile-label" style="left:88px;top:274px;font-size:4.5px">CHAPTER 2</div>
  <div class="abs tile-label" style="left:22px;top:331px;font-size:4.5px">CHAPTER 3</div>

  <h2 class="abs section-title" style="left:15px;top:364px;font-size:7px">EVENTS</h2>
  <div class="abs event-photo" role="img" aria-label="Modernes Gebäude mit Hotelschriftzug" style="left:15px;top:383px;width:110px;height:72px"></div>
  <div class="abs event-title" style="left:18px;top:465px;font-size:4.4px">GOTTES IDEE MIT DER AGENTUR K</div>
  <div class="abs event-date" style="left:18px;top:475px;font-size:4.4px">22/03/2019</div>
  <div class="abs event-venue" style="left:18px;top:486px;font-size:4.4px">ZUM ADLER | Birkenau</div>
  <svg class="abs" style="left:117px;top:486px" width="8" height="7" viewBox="0 0 7 6"><path d="M0 0l3 3-3 3M3 0l3 3-3 3" fill="none" stroke="var(--red)" stroke-width="1.2"/></svg>

  <div class="abs event-photo" role="img" aria-label="Gasthaus mit Terrasse und Sonnenschirmen" style="left:15px;top:509px;width:110px;height:73px"></div>
  <div class="abs event-title" style="left:18px;top:592px;font-size:4.4px">NÄCHSTE GENERALVERSAMMLUNG</div>
  <div class="abs event-date" style="left:18px;top:602px;font-size:4.4px">23/03/2019</div>
  <div class="abs event-venue" style="left:18px;top:612px;font-size:4.4px">AUBERGE DES PINS | Vallorbe</div>
  <svg class="abs" style="left:117px;top:612px" width="8" height="7" viewBox="0 0 7 6"><path d="M0 0l3 3-3 3M3 0l3 3-3 3" fill="none" stroke="var(--red)" stroke-width="1.2"/></svg>

  <footer class="abs footer" style="left:0;top:644px;width:140px;height:131px;text-align:center;font-size:4.8px;line-height:7.2px">
    <div style="margin-top:26px;font-weight:700">KRTWLE</div>
    <div style="margin-top:8px">Kreis Treuer Wirtschafts<br>Leute<br>Europa</div>
    <div style="margin-top:11px">info@krtwle.de<br>www.krtwle.com</div>
    <div style="margin-top:11px">Datenschutz<br>Impressum</div>
  </footer>
</section>

</body>
</html>
```